Fresh & Clean *NEW* BUSINESS CARD Needed - OPTOMETRY Clinic/Optical

High-tech optometry practice with 3 doctors seeking new business card.  We provide eye exams, sell, designer glasses/contacts/specialty eyewear and treat ocular diseases.  For our business cards, we are seeking fresh, clean, and crisp design as we grow our team (staffing change).  Simply adding doctors is making the card look busy/cluttered.
 Looking for professional, less cluttered look yet still have our logo, doctor names, phone, address, and website....If possible!  :)
Names:
Marcia Trelford, O.D.
Ned Pallister, O.D.
Oona Ferrant, O.D.
Phone: 555-014-2738
Website: www.BrightLensHub.example
Address:  417 Garnet R. Holloway, Fernhollow, ST 00000
Ultimately we have the main business card with all doctor sames and that card has two versions  (front is always the same).  The back has two designs (1) displays next appointment time/date, (2) for "general use" (non-appointment.)    I have attached what we have used in the past.  
We also need a design template for each team member in our practice with their name, title, and email.   Those should be designed with the "general use" back (see attached).
**Open to entirely new design so don't feel obligated to keep current format.  Need new perspective!  Also including our watermark and some other design features we have consistently used in past in our portfolio.  Included are two options for logos--vertical and horizontal.
**I also would like to remove "Member of Sight Alliance" on our logo if possible**
 Other image files available upon request.

Target Market(s)

New patient & Current Patients

Industry/Entity Type

Optometry

Contact Information for Business Card

High-tech optometry practice with 3 doctors seeking new business card.  We provide eye exams, sell, designer glasses/contacts/specialty eyewear and treat ocular diseases.  For our business cards, we are seeking fresh, clean, and crisp design as we grow our team (staffing change).  Simply adding doctors is making the card look busy/cluttered.  Looking for professional, less cluttered look yet still have our logo, doctor names, phone, address, and website....If possible!  :) Names: Marcia Trelford, O.D. Ned Pallister, O.D. Oona Ferrant, O.D. Phone: 555-014-2738 Website: www.BrightLensHub.example Address:  417 Garnet R. Holloway, Fernhollow, ST 00000 Ultimately we have the main business card with all doctor sames and that card has two versions  (front is always the same).  The back has two designs (1) displays next appointment time/date, (2) for "general use" (non-appointment.)    I have attached what we have used in the past.   We also need a design template for each team member in our practice with their name, title, and email.   Those should be designed with the "general use" back (see attached). **Open to entirely new design so don't feel obligated to keep current format.  Need new perspective!  Also including our watermark and some other design features we have consistently used in past in our portfolio.  Included are two options for logos--vertical and horizontal. **I also would like to remove "Member of Sight Alliance" on our logo if possible**  Other image files available upon request.

Font styles to use
Other font styles liked:
• We have used Montserrat / Yellowtail in the past

Colors

Designer to choose colors to be used in the design.

Requirements
Must have
• Clean & Fresh Design with Logo / Info provided in description. Horizontal orientation. **I have included the CMYK colors we currently have in our logo.
Should not have
• Cluttered

```html
<!DOCTYPE html>
<html lang="en">
<head>
<meta charset="utf-8">
<title>brightlenshub – business cards</title>
<link href="https://fonts.googleapis.com/css2?family=Montserrat:wght@400;500;600&family=Yellowtail&display=swap" rel="stylesheet">
<style>
  :root {
    --backdrop: #d9dbdb;
    --card: #ffffff;
    --grey: #6d6e70;
    --gold: #dcb306;
    --sky: #a4dce8;
    --olive: #99a24a;
    --brown: #6b2d16;
    --steel: #587688;
    --ink: #333333;
  }
  * { margin: 0; padding: 0; box-sizing: border-box; }
  html, body { width: 1200px; height: 1200px; overflow: hidden; background: var(--backdrop); }
  body { position: relative; font-family: "Montserrat", sans-serif; }

  .card {
    position: absolute; left: 309px; width: 581px; height: 348px;
    background: var(--card);
    box-shadow: 0 3px 5px rgba(0,0,0,0.28);
  }
  .card--front { top: 46px; }
  .card--appointment { top: 424px; }
  .card--general { top: 802px; }

  .brand-mark { position: absolute; border-radius: 50%; background: var(--sky); }
  .wordmark { position: absolute; color: var(--grey); font-weight: 400; white-space: nowrap; line-height: 1; }

  .card--front .brand-mark { left: 150px; top: 31px; width: 44px; height: 44px; }
  .card--front .wordmark { left: 215px; top: 38px; font-size: 28px; letter-spacing: 1px; }

  .doctors { position: absolute; left: 38px; top: 106px; font-family: "Yellowtail", cursive; color: var(--brown); font-size: 27px; line-height: 31px; letter-spacing: 1px; }

  .color-rule { position: absolute; height: 3px; display: flex; }
  .color-rule span { height: 100%; }
  .color-rule .seg-grey { background: var(--grey); width: 38.2%; }
  .color-rule .seg-gold { background: var(--gold); width: 17.9%; }
  .color-rule .seg-brown { background: var(--brown); width: 9%; }
  .color-rule .seg-olive { background: var(--olive); width: 11.1%; }
  .color-rule .seg-sky { background: var(--sky); width: 18.1%; }
  .color-rule .seg-steel { background: var(--steel); width: 5.7%; }
  .card--front .color-rule { left: 38px; top: 212px; width: 371px; }

  .contact { position: absolute; left: 39px; top: 228px; list-style: none; color: var(--brown); font-size: 17px; }
  .contact li { display: flex; align-items: center; height: 26px; }
  .contact svg { width: 15px; height: 15px; margin-right: 11px; fill: var(--gold); flex: none; }

  .dot-column { position: absolute; left: 55px; top: 0; }
  .dot-column span { position: absolute; border-radius: 50%; transform: translate(-50%, -50%); }
  .dot-column .d1 { top: 71px; width: 34px; height: 34px; background: var(--gold); }
  .dot-column .d2 { top: 115px; width: 29px; height: 29px; background: var(--sky); }
  .dot-column .d3 { top: 158px; width: 22px; height: 22px; background: var(--olive); }
  .dot-column .d4 { top: 202px; width: 14px; height: 14px; background: var(--brown); }
  .dot-column .d5 { top: 247px; width: 10px; height: 10px; background: var(--steel); }
  .dot-column .d6 { top: 290px; width: 6px; height: 6px; background: var(--grey); }

  .card--appointment .brand-mark { left: 253px; top: 48px; width: 60px; height: 60px; }
  .card--appointment .wordmark { left: 100px; top: 125px; width: 371px; text-align: center; font-size: 52px; }
  .card--appointment .color-rule { left: 100px; top: 190px; width: 371px; }

  .appointment-banner { position: absolute; left: 116px; top: 206px; width: 340px; height: 30px; background: var(--olive); color: #fff; font-weight: 600; font-size: 20px; text-align: center; line-height: 30px; letter-spacing: 0.3px; }
  .field-label { position: absolute; top: 252px; color: var(--grey); font-weight: 600; font-size: 16px; }
  .field-label--date { left: 153px; }
  .field-label--time { left: 380px; }

  .card--general .brand-mark { left: 259px; top: 63px; width: 60px; height: 60px; }
  .card--general .wordmark { left: 105px; top: 142px; width: 370px; text-align: center; font-size: 52px; }
  .card--general .color-rule { left: 105px; top: 205px; width: 370px; }
  .services { position: absolute; left: 90px; top: 226px; width: 400px; text-align: center; color: var(--ink); font-size: 16.5px; line-height: 20.5px; }
</style>
</head>
<body>

<section class="card card--front">
  <span class="brand-mark"></span>
  <div class="wordmark">brightlenshub</div>
  <div class="doctors">
    <p>Marcia Trelford, O.D.</p>
    <p>Ned Pallister, O.D.</p>
    <p>Oona Ferrant, O.D.</p>
  </div>
  <div class="color-rule"><span class="seg-grey"></span><span class="seg-gold"></span><span class="seg-brown"></span><span class="seg-olive"></span><span class="seg-sky"></span><span class="seg-steel"></span></div>
  <ul class="contact">
    <li><svg viewBox="0 0 24 24"><path d="M6.6 10.8a15.1 15.1 0 0 0 6.6 6.6l2.2-2.2a1 1 0 0 1 1-.25 11.4 11.4 0 0 0 3.6.57 1 1 0 0 1 1 1V20a1 1 0 0 1-1 1A17 17 0 0 1 3 4a1 1 0 0 1 1-1h3.5a1 1 0 0 1 1 1c0 1.25.2 2.45.57 3.57a1 1 0 0 1-.25 1z"/></svg>555-014-2738</li>
    <li><svg viewBox="0 0 24 24"><path d="M12 2a10 10 0 1 0 0 20 10 10 0 0 0 0-20zm0 2c.9 0 2.2 1.9 2.8 5H9.2C9.8 5.9 11.1 4 12 4zM4.3 11h3.8c.05-1 .1-1.3.2-2H5a8 8 0 0 0-.7 2zm0 2a8 8 0 0 0 .7 2h3.3c-.1-.7-.15-1-.2-2zm5.8 0c.05 1 .1 1.3.2 2h3.4c.1-.7.15-1 .2-2zm0-2h3.8c-.05-1-.1-1.3-.2-2h-3.4c-.1.7-.15 1-.2 2zm5.8 0h3.8a8 8 0 0 0-.7-2h-3.3c.1.7.15 1 .2 2zm0 2c-.05 1-.1 1.3-.2 2H19a8 8 0 0 0 .7-2zM12 20c-.9 0-2.2-1.9-2.8-5h5.6c-.6 3.1-1.9 5-2.8 5z"/></svg>www.BrightLensHub.example</li>
    <li><svg viewBox="0 0 24 24"><path d="M12 2a7 7 0 0 0-7 7c0 5.2 7 13 7 13s7-7.8 7-13a7 7 0 0 0-7-7zm0 9.5A2.5 2.5 0 1 1 12 6.5a2.5 2.5 0 0 1 0 5z"/></svg>417 Garnet R. Holloway, Fernhollow, ST 00000</li>
  </ul>
</section>

<section class="card card--appointment">
  <div class="dot-column"><span class="d1"></span><span class="d2"></span><span class="d3"></span><span class="d4"></span><span class="d5"></span><span class="d6"></span></div>
  <span class="brand-mark"></span>
  <div class="wordmark">brightlenshub</div>
  <div class="color-rule"><span class="seg-grey"></span><span class="seg-gold"></span><span class="seg-brown"></span><span class="seg-olive"></span><span class="seg-sky"></span><span class="seg-steel"></span></div>
  <div class="appointment-banner">Your Next Appointment</div>
  <div class="field-label field-label--date">Date</div>
  <div class="field-label field-label--time">Time</div>
</section>

<section class="card card--general">
  <div class="dot-column"><span class="d1"></span><span class="d2"></span><span class="d3"></span><span class="d4"></span><span class="d5"></span><span class="d6"></span></div>
  <span class="brand-mark"></span>
  <div class="wordmark">brightlenshub</div>
  <div class="color-rule"><span class="seg-grey"></span><span class="seg-gold"></span><span class="seg-brown"></span><span class="seg-olive"></span><span class="seg-sky"></span><span class="seg-steel"></span></div>
  <p class="services">We provide eye exams,<br>sell, designer glasses/contacts/specialty<br>eyewear and treat ocular diseases.</p>
</section>

</body>
</html>
```